We are a music company that specializes in Music Mixing and Mastering. We also do vocal recording and create instrumentals for various artists. Our website is 731kv.com

Target Market(s)

Musicians, Record labels, rappers, and singers

Industry/Entity Type

Artists

Contact Information for Business Card

731KV
Industry Standard Mixing & Mastering
(484) 317-2095
sales@731kv.com
731kv.com

Requirements
Must have
• contact info and twitter (@731KV)

```html
<!DOCTYPE html>
<html lang="en">
<head>
<meta charset="utf-8">
<title>731KV Business Cards</title>
<link rel="stylesheet" href="https://fonts.googleapis.com/css2?family=Ubuntu:wght@300;400;500&display=swap">
<style>
  :root {
    --backdrop: #3a3a3c;
    --card-dark: #1c1c1e;
    --card-dark-2: #262628;
    --band-white: #f4f4f4;
    --ink-black: #151515;
    --ink-grey: #4a4a4a;
    --text-light: #d9d9d9;
    --text-white: #ffffff;
    --accent-blue: #1aa3e8;
    --photo-blue: #1e6f9a;
    --photo-grey: #8a8f94;
  }
  * { box-sizing: border-box; margin: 0; padding: 0; }
  html, body {
    width: 1200px; height: 1000px; overflow: hidden;
    background: var(--backdrop);
    font-family: "Ubuntu", sans-serif;
  }
  .stage { position: relative; width: 1200px; height: 1000px; }

  .card {
    position: absolute;
    width: 560px; height: 320px;
    background: var(--card-dark);
    clip-path: polygon(34px 0, 100% 0, 100% calc(100% - 34px), calc(100% - 34px) 100%, 0 100%, 0 34px);
    overflow: hidden;
  }
  .card--contact { left: 70px; top: 150px; }
  .card--brand { left: 570px; top: 520px; }

  .pixel-field {
    position: absolute; left: 0; right: 0; bottom: 0;
    background: linear-gradient(180deg, var(--card-dark-2) 0%, var(--card-dark) 100%);
  }

  /* contact side */
  .console-photo {
    position: absolute; left: 0; top: 0; width: 100%; height: 150px;
    background: linear-gradient(100deg, var(--photo-grey) 0%, var(--photo-blue) 45%, #15557a 70%, #cfd3d6 100%);
  }
  .card--contact .pixel-field { top: 150px; }
  .brand-name {
    font-weight: 500; letter-spacing: 1px; line-height: 1;
  }
  .card--contact .brand-name {
    position: absolute; right: 40px; top: 30px;
    font-size: 44px; color: var(--text-white);
  }
  .card--contact .site-url {
    position: absolute; left: 30px; top: 118px;
    font-size: 15px; color: var(--text-white);
  }
  .contact-block {
    position: absolute; left: 30px; top: 178px;
    color: var(--text-light); font-size: 15px; line-height: 1.35;
  }
  .contact-row { display: flex; gap: 14px; align-items: flex-start; }
  .contact-row + .contact-row { margin-top: 16px; }
  .icon-square {
    width: 20px; height: 20px; flex: none; margin-top: 2px;
    background: var(--accent-blue); border-radius: 2px;
  }
  .contact-lines p { margin: 0; }

  /* brand side */
  .white-band {
    position: absolute; left: 0; right: 0; top: 30px; height: 160px;
    background: var(--band-white);
  }
  .card--brand .pixel-field { top: 190px; }
  .card--brand .brand-name {
    position: absolute; left: 38px; top: 58px;
    font-size: 58px; color: var(--ink-black);
  }
  .card--brand .site-url {
    position: absolute; left: 40px; top: 140px;
    font-size: 14px; color: var(--ink-grey);
  }
  .blue-pixels {
    position: absolute; right: 0; top: 30px; width: 150px; height: 160px;
    background: linear-gradient(90deg, rgba(26,163,232,0) 0%, var(--accent-blue) 45%);
  }
</style>
</head>
<body>
<main class="stage">

  <section class="card card--contact" aria-label="Business card, contact side">
    <div class="console-photo" role="img" aria-label="Photo of a studio mixing console with faders, tinted blue"></div>
    <div class="pixel-field" role="img" aria-label="Dark pixel equalizer pattern"></div>
    <div class="brand-name">731KV</div>
    <div class="site-url">www.731kv.com</div>
    <div class="contact-block">
      <div class="contact-row">
        <span class="icon-square" aria-hidden="true"></span>
        <div class="contact-lines">
          <p>731KV Industry Standard Mixing &amp; Mastering</p>
          <p>(484) 317-2095</p>
          <p>sales@731kv.com</p>
        </div>
      </div>
      <div class="contact-row">
        <span class="icon-square" aria-hidden="true"></span>
        <div class="contact-lines"><p>@731KV</p></div>
      </div>
    </div>
  </section>

  <section class="card card--brand" aria-label="Business card, brand side">
    <div class="white-band"></div>
    <div class="blue-pixels" role="img" aria-label="Blue pixel equalizer pattern"></div>
    <div class="pixel-field" role="img" aria-label="Dark pixel equalizer pattern"></div>
    <div class="brand-name">731KV</div>
    <div class="site-url">www.731kv.com</div>
  </section>

</main>
</body>
</html>
```